Medical Billing Company Needs a Business Card Design

We need a business card design for a Florida based medical billing company called 'Lorrimer Tallbrook Services'. We specialize in providing revenue cycle management services to physician and therapist offices (we're basically their back-office processing partner for providing billing software, claims submissions, A/R follow-up and patient statements & collections. Our logo is red and blue-ish, so make sure that whatever other elements are used will match appropriately. Our current business card design has a too small font size. I'd like to project an image that shows we are modern & reliable. On a side note, I'm planning on using VUX for printing these cards.

Target Market(s)

Office managers, physicians, therapists

Industry/Entity Type

Printing

Requirements
Must have
• Logo
Name of Employee
Phone
Fax
E-mail
Website

```html
<!DOCTYPE html>
<html lang="en">
<head>
<meta charset="utf-8">
<title>Lorrimer Tallbrook Services – Business Card</title>
<link rel="stylesheet" href="https://fonts.googleapis.com/css2?family=Source+Sans+3:wght@400;600;700&display=swap">
<style>
  :root {
    --navy: #2f2a7a;
    --violet: #4a3f93;
    --brand-red: #a8272c;
    --red-light: #b9403f;
    --ink: #3a3a3a;
    --rule: #b8b8b8;
    --paper: #ffffff;
    --backdrop: #e9e9ee;
  }
  * { box-sizing: border-box; margin: 0; padding: 0; }
  html, body {
    width: 1200px; height: 987px; overflow: hidden;
    background: var(--backdrop);
    font-family: "Source Sans 3", "Helvetica Neue", Arial, sans-serif;
  }
  .sheet {
    position: relative; width: 1200px; height: 987px;
    display: flex; align-items: center; justify-content: center; gap: 40px;
  }
  .card {
    position: relative; width: 540px; height: 310px;
    border-radius: 22px; overflow: hidden;
    box-shadow: 0 10px 30px rgba(0,0,0,0.18);
  }

  /* Front */
  .card-front { background: var(--paper); }
  .card-front .swoosh { position: absolute; inset: 0; }
  .wordmark {
    position: absolute; top: 24px; left: 60px;
    font-weight: 400; font-size: 38px; letter-spacing: 1px; line-height: 1;
    color: var(--navy); text-transform: uppercase;
  }
  .wordmark .line-2 { display: block; margin-left: 150px; margin-top: 4px; }
  .holder {
    position: absolute; top: 118px; left: 120px;
    font-size: 21px; color: var(--violet);
  }
  .holder .name { font-weight: 700; }
  .holder .role { color: var(--brand-red); }
  .address {
    position: absolute; top: 160px; left: 70px; width: 150px;
    font-size: 15px; line-height: 1.3; color: var(--ink); text-align: right;
  }
  .divider {
    position: absolute; top: 160px; left: 234px; width: 1px; height: 62px;
    background: var(--rule);
  }
  .contacts {
    position: absolute; top: 157px; left: 248px; list-style: none;
    font-size: 16px; line-height: 1.35; color: var(--ink);
  }
  .contacts li { display: flex; align-items: center; gap: 7px; }
  .contacts svg { width: 12px; height: 12px; fill: var(--ink); }
  .front-web {
    position: absolute; left: 28px; bottom: 16px;
    font-size: 17px; color: var(--paper); letter-spacing: .3px;
  }

  /* Back */
  .card-back {
    background: radial-gradient(circle at 50% 45%, var(--red-light), var(--brand-red) 75%);
    color: var(--paper); text-align: center;
  }
  .tagline {
    position: absolute; top: 26px; left: 0; right: 0;
    font-size: 14px; font-weight: 600; letter-spacing: 1.5px; text-transform: uppercase;
  }
  .back-mark {
    position: absolute; top: 118px; left: 0; right: 0;
    font-size: 34px; font-weight: 400; letter-spacing: 2px; text-transform: uppercase;
  }
  .back-web {
    position: absolute; bottom: 30px; left: 0; right: 0;
    font-size: 17px; letter-spacing: 3px;
  }
</style>
</head>
<body>
<main class="sheet">
  <section class="card card-front" aria-label="Card front">
    <svg class="swoosh" viewBox="0 0 540 310" preserveAspectRatio="none" aria-hidden="true">
      <path d="M0 238 C160 248 320 272 540 302 L540 306 C320 277 160 254 0 245 Z" fill="var(--brand-red)"/>
      <path d="M0 252 C150 258 320 280 430 310 L0 310 Z" fill="var(--navy)"/>
      <path d="M0 258 C150 266 300 286 390 310 L0 310 Z" fill="var(--violet)" opacity=".55"/>
    </svg>

    <div class="wordmark"><span class="line-1">Lorrimer</span><span class="line-2">Tallbrook</span></div>

    <p class="holder"><span class="name">Daniel Okafor,</span> CHBME, <span class="role">President</span></p>

    <p class="address">2870 SW Harbor Rd<br>Seabridge, FL 34021</p>
    <div class="divider"></div>
    <ul class="contacts">
      <li><svg viewBox="0 0 12 12"><path d="M2.5 1 L4.5 1 L5.2 3.6 L4 4.6 C4.6 6 5.9 7.4 7.4 8 L8.4 6.8 L11 7.5 L11 9.5 C11 10.3 10.3 11 9.5 11 C5 11 1 7 1 2.5 C1 1.7 1.7 1 2.5 1 Z"/></svg>555-014-0789</li>
      <li><svg viewBox="0 0 12 12"><path d="M3 0 H9 V12 H3 Z M4 1.5 V7 H8 V1.5 Z"/></svg>555-014-0789</li>
      <li><svg viewBox="0 0 12 12"><path d="M0 2 H12 V10 H0 Z M1 3 L6 7 L11 3 Z" fill-rule="evenodd"/></svg>info@lorrimertallbrook.com</li>
    </ul>

    <p class="front-web">www.lorrimertallbrook.net</p>
  </section>

  <section class="card card-back" aria-label="Card back">
    <p class="tagline">Medical Billing for Healthcare Professionals</p>
    <p class="back-mark">Lorrimer Tallbrook</p>
    <p class="back-web">www.lorrimertallbrook.net</p>
  </section>
</main>
</body>
</html>
```